Visitenkarten-Design für Immobilienmakler
Zielgruppe
Immobilienmakler
Aufgabenstellung
Top moderne hochwertige Visitenkate, wir hätten gerne eine sehr hochwertig moderne Visitenkarte mit Bild vom Mitarbeiter... Anbei habe ich die alte Visitenkarte die ich sehr kindlich finde... Es sollte jetzt sehr exklusive aussehen. Alle Daten können von der alten Visitenkarte übernommen werden.. danke

```html
<!DOCTYPE html>
<html lang="de">
<head>
<meta charset="utf-8">
<title>Velmar Agentur – Visitenkarte</title>
<link href="https://fonts.googleapis.com/css2?family=Mulish:wght@400;700;800&display=swap" rel="stylesheet">
<style>
  :root {
    --stage: #2d2d2c;
    --green-light: #0a4a22;
    --green-dark: #011a0b;
    --icon-green: #0e7a35;
    --gold: #a87d2a;
    --ink: #1c1c1c;
    --white: #ffffff;
  }
  * { margin: 0; padding: 0; box-sizing: border-box; }
  html, body { width: 935px; height: 1200px; overflow: hidden; }
  body {
    background: var(--stage);
    font-family: "Mulish", "Avenir", sans-serif;
    position: relative;
  }
  .card {
    position: absolute;
    width: 541px;
    height: 350px;
    box-shadow: 0 10px 28px rgba(0,0,0,0.55);
    overflow: hidden;
  }
  .card--front {
    left: 208px; top: 198px;
    background: radial-gradient(ellipse 60% 65% at 50% 48%, var(--green-light) 0%, #053418 45%, var(--green-dark) 100%);
  }
  .card--back {
    left: 214px; top: 670px; width: 543px;
    background: var(--white);
  }
  .brand {
    position: absolute;
    color: var(--white);
    text-align: right;
  }
  .brand__name {
    font-weight: 800;
    letter-spacing: -0.5px;
    line-height: 1;
    display: block;
  }
  .brand__tag {
    font-weight: 400;
    text-transform: uppercase;
    letter-spacing: 0.6px;
    display: block;
  }
  .card--front .brand { left: 0; right: 0; top: 150px; text-align: center; }
  .card--front .brand__name { font-size: 36px; }
  .card--front .brand__tag { font-size: 9px; margin-top: 6px; padding-left: 140px; }

  .back__panel {
    position: absolute; left: 0; top: 0;
    width: 266px; height: 350px;
    background: radial-gradient(ellipse 75% 65% at 50% 55%, #08461f 0%, #04311a 45%, var(--green-dark) 100%);
  }
  .portrait {
    position: absolute;
    left: 54px; top: 70px;
    width: 148px; height: 148px;
    border-radius: 50%;
    border: 8px solid var(--gold);
    background: radial-gradient(circle at 50% 45%, #ffffff 0%, #f1f1f1 60%, #dcdcdc 100%);
  }
  .back__panel .brand { left: 48px; top: 276px; }
  .back__panel .brand__name { font-size: 24px; }
  .back__panel .brand__tag { font-size: 6px; margin-top: 4px; }

  .person {
    position: absolute; left: 292px; top: 68px;
    color: var(--ink);
  }
  .person__name { font-size: 19px; font-weight: 800; line-height: 1.1; }
  .person__role { font-size: 15px; font-weight: 400; line-height: 19px; margin-top: 6px; }

  .contact { position: absolute; left: 0; top: 0; width: 543px; height: 350px; list-style: none; }
  .contact__item {
    position: absolute; left: 292px;
    font-size: 15px; color: var(--ink); line-height: 19px;
  }
  .contact__icon {
    position: absolute; left: -48px;
    width: 28px; height: 28px; border-radius: 50%;
    background: var(--icon-green);
    display: flex; align-items: center; justify-content: center;
  }
  .contact__item--address { top: 173px; }
  .contact__item--web { top: 206px; }
  .contact__item--mail { top: 243px; }
  .contact__item--phone { top: 274px; }
  .contact__item--address .contact__icon,
  .contact__item--web .contact__icon,
  .contact__item--mail .contact__icon { top: -4px; }
  .contact__item--phone .contact__icon { top: 3px; }
</style>
</head>
<body>
  <section class="card card--front">
    <div class="brand">
      <span class="brand__name">Velmar Agentur</span>
      <span class="brand__tag">Der Immobilienmakler</span>
    </div>
  </section>

  <section class="card card--back">
    <div class="back__panel">
      <div class="portrait" role="img" aria-label="Porträtfoto des Geschäftsführers im weißen Hemd"></div>
      <div class="brand">
        <span class="brand__name">Velmar Agentur</span>
        <span class="brand__tag">Der Immobilienmakler</span>
      </div>
    </div>

    <div class="person">
      <p class="person__name">Lukas Brandtner</p>
      <p class="person__role">Dipl. Immobilienmanager<br>Geschäftsführer</p>
    </div>

    <ul class="contact">
      <li class="contact__item contact__item--address">
        <span class="contact__icon"><svg width="14" height="16" viewBox="0 0 14 16"><path d="M7 1a5 5 0 0 0-5 5c0 3.6 5 9 5 9s5-5.4 5-9a5 5 0 0 0-5-5zm0 7a2 2 0 1 1 0-4 2 2 0 0 1 0 4z" fill="#fff"/></svg></span>
        Am Feldweg 12 | 6850 Dornbach
      </li>
      <li class="contact__item contact__item--web">
        <span class="contact__icon"><svg width="16" height="16" viewBox="0 0 16 16" fill="none" stroke="#fff" stroke-width="1.3"><circle cx="8" cy="8" r="6.3"/><ellipse cx="8" cy="8" rx="2.8" ry="6.3"/><path d="M1.7 8h12.6M2.7 4.8h10.6M2.7 11.2h10.6"/></svg></span>
        www.velmar-agentur.com
      </li>
      <li class="contact__item contact__item--mail">
        <span class="contact__icon"><svg width="16" height="12" viewBox="0 0 16 12" fill="none" stroke="#fff" stroke-width="1.3"><rect x="1" y="1" width="14" height="10" rx="1"/><path d="M1 1.5l7 5.5 7-5.5M1 10.5l5-4.5M15 10.5l-5-4.5"/></svg></span>
        lukas@velmar-agentur.com
      </li>
      <li class="contact__item contact__item--phone">
        <span class="contact__icon"><svg width="15" height="15" viewBox="0 0 24 24"><path d="M6.6 10.8a15.1 15.1 0 0 0 6.6 6.6l2.2-2.2a1 1 0 0 1 1-.25 11.4 11.4 0 0 0 3.6.57 1 1 0 0 1 1 1V20a1 1 0 0 1-1 1A17 17 0 0 1 3 4a1 1 0 0 1 1-1h3.5a1 1 0 0 1 1 1c0 1.25.2 2.45.57 3.6a1 1 0 0 1-.25 1z" fill="#fff"/></svg></span>
        +43 5500 12 345 67<br>+43 660 1234 567
      </li>
    </ul>
  </section>
</body>
</html>
```